PSD Only - Wordpress Magazine Theme Design

We need a design for our new Premuim wordpress Magazine theme design based on our basic wire-frame. The theme will be used by people who run online magazine, news website or just blog in general.

The layout of homepage is showing recent posts in many way which is easy to user to customize the section of their homepage to show their post based on various categories.

2 Page design need (Homepage and Single Post)
Updates

Project Deadline Extended
Reason: want to get more designer and I am off for holiday a few days too. Better extend the time for designers as well as me also.

Target Market(s)

General Blogger who want a nice premium theme as well as other content based wesite.

Industry/Entity Type

Online

Font styles to use
Sans Serif

Requirements
Must have
• + Must have 2 page design based on Wireframing. Homepage (home.png) annd Single Post (Single.png)
• + Layout must be based on wireframe.
• + Width 1025px
• + 2 Navigation Menu in Header Must be in different style. When theme goes public, user can choose to have both or only 1 navigation or completely hide both of them.
• + 2 Featured Content Slider as you see in wire-frame. They must be in different style from each other.
• + Those recent news section is only about arrange post in defferent ways which only include post feature image, post title as well as post meta info.
• + Sidebar Widget Must be 300px (not include margin or padding) in order to be able for user to place ads with (300px of width) in sidebar widget)
• + Footer Widget Section should have a bit different colour in order to look different for main layout.
Nice to have
• + Drop down Menu
• + (Optional) Some custom Widget (Based on your imagination and creativity)

```html
<!DOCTYPE html>
<html lang="en">
<head>
<meta charset="utf-8">
<title>Kite Magazine – Home</title>
<link href="https://fonts.googleapis.com/css2?family=Questrial&display=swap" rel="stylesheet">
<style>
:root{
  --blue:#1f9eea;
  --blue-dark:#1479bd;
  --ink:#222222;
  --dark:#1b1b1b;
  --nav:#1a1a1a;
  --text:#333333;
  --muted:#8a8a8a;
  --light:#f2f2f2;
  --line:#e4e4e4;
  --footer:#1f1f1f;
  --footer-text:#9a9a9a;
}
*{box-sizing:border-box;margin:0;padding:0}
html,body{width:1200px;height:4945px;overflow:hidden}
body{position:relative;background:#fff;font-family:"Questrial",sans-serif;color:var(--text)}
.abs{position:absolute}
a{color:inherit;text-decoration:none}

/* top bar */
.topbar{top:0;left:0;width:1200px;height:40px;background:var(--light)}
.topbar .links{position:absolute;left:132px;top:13px;display:flex;gap:30px;font-size:12px;color:#666}
.topbar .social{position:absolute;right:125px;top:11px;display:flex;gap:9px}
.topbar .social span{width:18px;height:18px;background:#c9c9c9;border-radius:3px}
.topbar .social span.on{background:var(--blue)}

/* header */
.brand{top:84px;left:132px}
.brand .name{font-size:38px;letter-spacing:2px;color:var(--ink);line-height:1}
.brand .tag{font-size:15px;color:var(--muted);margin-top:8px;letter-spacing:1px}
.header-ad{top:79px;left:402px;width:670px;height:79px;background:linear-gradient(90deg,#f4f7fb 0%,#e6eef7 55%,#2a2a2a 80%,#111 100%);border:1px solid #dde3ea}

/* nav */
.mainnav{top:195px;left:0;width:1200px;height:62px;background:var(--nav)}
.mainnav .home{position:absolute;left:125px;top:0;width:62px;height:62px;background:var(--blue);display:flex;align-items:center;justify-content:center}
.mainnav ul{position:absolute;left:208px;top:0;height:62px;display:flex;list-style:none;gap:34px;align-items:center;color:#fff;font-size:15px}
.mainnav .search{position:absolute;left:835px;top:13px;width:240px;height:36px;background:#fff;display:flex;justify-content:flex-end}
.mainnav .search i{width:36px;height:36px;background:#2a2a2a;display:flex;align-items:center;justify-content:center;border:2px solid #fff}

/* photo placeholders */
.ph-city{background:linear-gradient(160deg,#cfd8e2 0%,#8f9aa5 45%,#3d4650 100%)}
.ph-office{background:linear-gradient(135deg,#8c8f93 0%,#cfcac4 50%,#5d5f62 100%)}
.ph-warm{background:linear-gradient(135deg,#c9b8a4,#7d6b5a)}
.ph-blue{background:linear-gradient(135deg,#9fc3e2,#3f6f9e)}
.ph-paper{background:linear-gradient(135deg,#e8e6e2,#a7a39c)}
.ph-green{background:linear-gradient(135deg,#8fb98a,#3e6b3f)}
.ph-grey{background:linear-gradient(135deg,#dcdcdc,#9a9a9a)}
.ph-dark{background:linear-gradient(135deg,#5b6168,#23272b)}

/* slider 1 */
.hero{top:280px;left:125px;width:950px;height:445px;overflow:hidden}
.hero .caption{position:absolute;left:245px;top:142px;width:442px;height:138px;background:rgba(31,158,234,.88);color:#fff;text-align:center;padding-top:20px}
.hero .caption h2{font-weight:400;font-size:32px}
.hero .caption p{font-size:17px;margin-top:8px;opacity:.9}
.hero .corner{position:absolute;left:0;bottom:0}

/* slider 2 */
.feature{top:745px;left:125px;width:627px;height:343px;overflow:hidden}
.feature .shade{position:absolute;left:0;bottom:0;width:100%;height:140px;background:linear-gradient(180deg,rgba(0,0,0,0),rgba(0,0,0,.75))}
.feature .txt{position:absolute;left:18px;bottom:20px;color:#fff}
.feature .txt h2{font-weight:400;font-size:29px}
.feature .txt p{font-size:16px;margin-top:2px}
.feature .txt small{font-size:11px}
.dots{display:flex;gap:6px}
.dots span{width:9px;height:9px;border-radius:50%;background:#777}
.dots span.on{background:var(--blue)}
.feature .dots{position:absolute;right:18px;bottom:22px}

/* section heads */
.head{height:37px;background:var(--dark);color:#fff;font-size:15px;padding:10px 14px;position:relative}
.head.blue{background:var(--blue)}
.head .ctl{position:absolute;right:12px;top:13px;display:flex;gap:6px}
.head .ctl span{width:11px;height:11px;background:#555;border-radius:2px}
.head.blue .ctl span{background:#fff;border-radius:50%;width:8px;height:8px;opacity:.6}
.head.blue .ctl span.on{opacity:1}

.meta{font-size:11px;color:var(--muted)}
.meta b{font-weight:400;margin:0 6px;color:#ccc}
.excerpt{font-size:12px;color:var(--muted);line-height:1.55}
.title{color:var(--ink);font-weight:400}

/* latest news */
.latest{top:1111px;left:125px;width:627px}
.cards3{display:flex;gap:30px;margin-top:22px}
.cards3 .card{width:189px}
.cards3 .img{height:128px}
.cards3 h3{font-size:16px;margin:18px 0 6px}
.cards3 .excerpt{margin-top:6px}

/* our magazine */
.ourmag{top:1450px;left:125px;width:627px}
.cards2{display:flex;gap:31px;margin-top:30px}
.cards2 .card{width:298px}
.cards2 .img{height:164px}
.cards2 h3{font-size:17px;margin:25px 0 6px}
.cards2 .excerpt{margin-top:8px}

/* world news */
.world{top:1836px;left:125px;width:627px}
.world .body{display:flex;gap:20px;margin-top:26px}
.world .lead{width:343px}
.world .lead .img{height:168px}
.world .lead h3{font-size:19px;margin:22px 0 6px}
.world .lead .excerpt{margin-top:8px}
.mini{display:flex;gap:12px}
.mini .img{flex:none}
.mini h4{font-size:12px;font-weight:400;color:var(--ink);line-height:1.45}
.mini .meta{margin-top:5px}
.world .list{width:264px;display:flex;flex-direction:column;gap:12px}
.world .list .img{width:70px;height:50px}

/* recent news */
.recent{top:2258px;left:125px;width:627px}
.grid2{display:grid;grid-template-columns:298px 298px;column-gap:31px;row-gap:20px;margin-top:24px}
.grid2 .img{width:62px;height:58px}

/* recent magazine news */
.recmag{top:2680px;left:125px;width:627px}
.rm-item{display:flex;gap:18px;margin-top:20px}
.rm-item .img{width:261px;height:197px;flex:none}
.rm-item h3{font-size:19px;margin-top:2px}
.rm-item .meta{margin-top:8px}
.rm-item .excerpt{margin-top:14px}
.btn{display:inline-block;font-size:11px;color:#fff;background:var(--blue);padding:9px 16px;margin-top:14px}
.btn.dark{background:var(--dark)}
.metabar{border-top:1px solid var(--line);border-bottom:1px solid var(--line);height:38px;margin-top:22px;display:flex;align-items:center;gap:46px;font-size:11px;color:var(--muted);padding-left:20px;position:relative}
.metabar span{display:flex;align-items:center;gap:7px}
.metabar .love{position:absolute;right:0;color:var(--blue)}

/* featured blog */
.featblog{top:3300px;left:125px;width:627px}
.fb-item .img{height:191px;margin-top:26px}
.fb-item h3{font-size:20px;line-height:1.3;margin-top:20px}
.fb-item .meta{margin-top:8px}
.fb-item .excerpt{margin-top:12px}

.pager{top:4410px;left:125px;display:flex;gap:6px;align-items:center;font-size:10px;color:var(--muted)}
.pager span.n{width:22px;height:22px;display:flex;align-items:center;justify-content:center;background:#e2e2e2;color:#555;font-size:11px}
.pager span.n.on{background:var(--blue);color:#fff}

/* sidebar */
.side{left:791px;width:284px}
.rp-list{padding:14px 0}
.rp-list .item{border-bottom:1px solid var(--line);padding:10px 0 12px}
.rp-list h4{font-size:12px;font-weight:400;color:var(--ink);line-height:1.5}
.rp-list .meta{margin-top:10px}
.ad{background:linear-gradient(180deg,#f4f4f4,#dcdcdc)}
.cats{list-style:none;padding:14px 0 0 2px;font-size:13px;color:#555}
.cats li{display:flex;align-items:center;gap:10px;margin-bottom:12px}
.cats li i{width:11px;height:11px;border:1px solid #999;border-radius:50%;flex:none}
.cats li.on{color:var(--blue)}
.cats li.on i{background:var(--blue);border-color:var(--blue)}
.cats li.sub{padding-left:22px;font-size:11px;margin-bottom:8px}
.cats li.sub i{width:6px;height:6px;border:none;background:#aaa}
.pop{padding-top:18px;display:flex;flex-direction:column;gap:20px}
.pop .img{width:90px;height:72px}

/* footer */
.footer{top:4484px;left:0;width:1200px;height:369px;background:var(--footer);color:var(--footer-text)}
.fcol{position:absolute;top:50px}
.fcol h5{font-weight:400;font-size:15px;color:#fff;border-bottom:1px solid #3a3a3a;padding-bottom:12px;width:240px}
.fcol .name{font-size:30px;color:#fff;letter-spacing:2px;margin-top:34px}
.fcol .tag{font-size:14px;margin-top:4px}
.fcol p{font-size:11px;line-height:1.6;margin-top:16px;width:250px}
.fpost{display:flex;gap:12px;margin-top:18px}
.fpost .img{width:62px;height:62px;flex:none}
.fpost h6{font-weight:400;font-size:12px;color:#ddd;line-height:1.4}
.fpost small{font-size:10px}
.news input{width:210px;height:30px;border:none;padding-left:8px;font-family:inherit;font-size:10px}
.news .go{display:inline-block;width:30px;height:30px;background:var(--blue);vertical-align:top}
.fsocial{display:flex;gap:10px;margin-top:20px}
.fsocial span{width:18px;height:18px;border-radius:3px;background:#555}
.bottombar{top:4870px;left:0;width:1200px;height:75px;background:var(--light);font-size:12px;color:#666}
.bottombar .l{position:absolute;left:125px;top:30px}
.bottombar .r{position:absolute;right:125px;top:30px;display:flex;gap:12px}
</style>
</head>
<body>

<div class="abs topbar">
  <nav class="links"><a>About</a><a>Privacy</a><a>Contact</a><a>Login</a><a>Register</a></nav>
  <div class="social"><span></span><span></span><span></span><span></span><span class="on"></span><span></span></div>
</div>

<div class="abs brand">
  <div class="name">KITE MAGAZINE</div>
  <div class="tag">Premium News / Magazine</div>
</div>
<div class="abs header-ad" role="img" aria-label="Advertising banner for an app store with a phone offer"></div>

<div class="abs mainnav">
  <div class="home"><svg width="22" height="20" viewBox="0 0 22 20"><path d="M11 1 1 10h3v9h5v-6h4v6h5v-9h3z" fill="#fff"/></svg></div>
  <ul><li>Business</li><li>About</li><li>People</li><li>News</li><li>Our Categories</li><li>Forum</li></ul>
  <div class="search"><i><svg width="14" height="14" viewBox="0 0 14 14"><circle cx="6" cy="6" r="4.5" stroke="#fff" stroke-width="1.8" fill="none"/><path d="M9.5 9.5 13 13" stroke="#fff" stroke-width="1.8"/></svg></i></div>
</div>

<section class="abs hero ph-city" role="img" aria-label="Wide photo of a city street with blurred pedestrians">
  <div class="caption">
    <h2>At vereos et accusamus</h2>
    <p>Sustoodio dignissirem ipsum dolor sitame<br>April 6, 2015 posted by Admin.</p>
  </div>
  <svg class="corner" width="70" height="70" viewBox="0 0 70 70"><path d="M0 0 70 70H0z" fill="var(--blue)"/></svg>
</section>

<section class="abs feature ph-office" role="img" aria-label="Photo of two colleagues working together at a laptop">
  <div class="shade"></div>
  <div class="txt">
    <h2>At vereos et accusamus</h2>
    <p>Susto odio dignissirem ipsum dolor sitamenes.</p>
    <small>April 6, 2015</small>
  </div>
  <div class="dots"><span></span><span class="on"></span><span></span><span></span></div>
</section>

<!-- main column -->
<section class="abs latest">
  <div class="head">Latest News</div>
  <div class="cards3">
    <article class="card"><div class="img ph-blue" role="img" aria-label="Photo of hands over business papers"></div><h3 class="title">At vero eos et accusa</h3><div class="meta">Posted by jon<b>|</b>2 Comments<b>|</b>4 hours ago</div><p class="excerpt">Lorem Ipsum is simply dummy text of the printing.</p></article>
    <article class="card"><div class="img ph-warm" role="img" aria-label="Photo of a person writing notes"></div><h3 class="title">At vero eos et accusa</h3><div class="meta">Posted by jon<b>|</b>2 Comments<b>|</b>4 hours ago</div><p class="excerpt">Lorem Ipsum is simply dummy text of the printing.</p></article>
    <article class="card"><div class="img ph-paper" role="img" aria-label="Photo of a newspaper and coffee on a desk"></div><h3 class="title">At vero eos et accusa</h3><div class="meta">Posted by jon<b>|</b>2 Comments<b>|</b>4 hours ago</div><p class="excerpt">Lorem Ipsum is simply dummy text of the printing.</p></article>
  </div>
</section>

<section class="abs ourmag">
  <div class="head blue">Our Magazine News</div>
  <div class="cards2">
    <article class="card"><div class="img ph-grey" role="img" aria-label="Photo of a team meeting around a table"></div><h3 class="title">On the other hand we denounc</h3><div class="meta">Posted by jon<b>|</b>2 Comments<b>|</b>4 hours ago</div><p class="excerpt">At vero eos et accusamus et iusto odio adisantimus duimus qui blanditiis praesentium.</p></article>
    <article class="card"><div class="img ph-blue" role="img" aria-label="Photo of hands pointing at printed charts"></div><h3 class="title">On the other hand we denounc</h3><div class="meta">Posted by jon<b>|</b>2 Comments<b>|</b>4 hours ago</div><p class="excerpt">At vero eos et accusamus et iusto odio adisantimus duimus qui blanditiis praesentium.</p></article>
  </div>
</section>

<section class="abs world">
  <div class="head">World News<div class="ctl"><span></span><span></span></div></div>
  <div class="body">
    <article class="lead"><div class="img ph-paper" role="img" aria-label="Photo of a man reading a newspaper"></div><h3 class="title">On the other hand we loreim ipdeno</h3><div class="meta">Posted by jon<b>|</b>2 Comments<b>|</b>4 hours ago</div><p class="excerpt">At vero eos et accusamus et iusto odio adisantimus duimus qui blanditiis praesentium eos et accusamus est eos et accusamus et.</p></article>
    <div class="list">
      <div class="mini"><div class="img ph-blue" role="img" aria-label="Thumbnail of an office"></div><div><h4>At vero eos et accusamus et iusto odio dignissimo...</h4><div class="meta">3 minute ago<b>|</b>0 comments</div></div></div>
      <div class="mini"><div class="img ph-warm" role="img" aria-label="Thumbnail of a reader"></div><div><h4>At vero eos et accusamus et iusto odio dignissimo...</h4><div class="meta">3 minute ago<b>|</b>0 comments</div></div></div>
      <div class="mini"><div class="img ph-grey" role="img" aria-label="Thumbnail of a laptop"></div><div><h4>At vero eos et accusamus et iusto odio dignissimo...</h4><div class="meta">3 minute ago<b>|</b>0 comments</div></div></div>
      <div class="mini"><div class="img ph-dark" role="img" aria-label="Thumbnail of a phone screen"></div><div><h4>At vero eos et accusamus et iusto odio dignissimo...</h4><div class="meta">3 minute ago<b>|</b>0 comments</div></div></div>
      <div class="mini"><div class="img ph-paper" role="img" aria-label="Thumbnail of papers"></div><div><h4>At vero eos et accusamus et iusto odio dignissimo...</h4><div class="meta">3 minute ago<b>|</b>0 comments</div></div></div>
    </div>
  </div>
</section>

<section class="abs recent">
  <div class="head blue">Recent News</div>
  <div class="grid2">
    <div class="mini"><div class="img ph-dark" role="img" aria-label="Thumbnail of a city at night"></div><div><h4>At vero eos et accusamus et iusto odio dignissimo...</h4><div class="meta">3 minute ago<b>|</b>0 comments</div></div></div>
    <div class="mini"><div class="img ph-warm" role="img" aria-label="Thumbnail of a person at work"></div><div><h4>At vero eos et accusamus et iusto odio dignissimo...</h4><div class="meta">3 minute ago<b>|</b>0 comments</div></div></div>
    <div class="mini"><div class="img ph-blue" role="img" aria-label="Thumbnail of a building"></div><div><h4>At vero eos et accusamus et iusto odio dignissimo...</h4><div class="meta">3 minute ago<b>|</b>0 comments</div></div></div>
    <div class="mini"><div class="img ph-grey" role="img" aria-label="Thumbnail of a desk"></div><div><h4>At vero eos et accusamus et iusto odio dignissimo...</h4><div class="meta">3 minute ago<b>|</b>0 comments</div></div></div>
    <div class="mini"><div class="img ph-green" role="img" aria-label="Thumbnail of a park"></div><div><h4>At vero eos et accusamus et iusto odio dignissimo...</h4><div class="meta">3 minute ago<b>|</b>0 comments</div></div></div>
    <div class="mini"><div class="img ph-paper" role="img" aria-label="Thumbnail of a notebook"></div><div><h4>At vero eos et accusamus et iusto odio dignissimo...</h4><div class="meta">3 minute ago<b>|</b>0 comments</div></div></div>
    <div class="mini"><div class="img ph-office" role="img" aria-label="Thumbnail of a meeting"></div><div><h4>At vero eos et accusamus et iusto odio dignissimo...</h4><div class="meta">3 minute ago<b>|</b>0 comments</div></div></div>
    <div class="mini"><div class="img ph-dark" role="img" aria-label="Thumbnail of a screen"></div><div><h4>At vero eos et accusamus et iusto odio dignissimo...</h4><div class="meta">3 minute ago<b>|</b>0 comments</div></div></div>
  </div>
</section>

<section class="abs recmag">
  <div class="head">Recent Magazine News<div class="ctl"><span></span><span></span></div></div>
  <article>
    <div class="rm-item"><div class="img ph-dark" role="img" aria-label="Photo of a tablet showing news on a desk"></div><div><h3 class="title">On the other hand we loreim ipdeno</h3><div class="meta">Posted by jon<b>|</b>2 Comments<b>|</b>4 hours ago</div><p class="excerpt">At vero eos et accusamus et iusto odio adisantimus duimus qui blanditiis praesentium eos et accusamus est eos et accusamus et.</p><a class="btn">READ MORE</a></div></div>
    <div class="metabar"><span>▦ June 11, 2015</span><span>▭ 22 Comments</span><span>◈ Public_News</span><span>◉ 124 Views</span><span class="love">♥ 12</span></div>
  </article>
  <article>
    <div class="rm-item"><div class="img ph-warm" role="img" aria-label="Photo of a woman smiling while using a laptop"></div><div><h3 class="title">On the other hand we loreim ipdeno</h3><div class="meta">Posted by jon<b>|</b>2 Comments<b>|</b>4 hours ago</div><p class="excerpt">At vero eos et accusamus et iusto odio adisantimus duimus qui blanditiis praesentium eos et accusamus est eos et accusamus et.</p><a class="btn">READ MORE</a></div></div>
    <div class="metabar"><span>▦ June 11, 2015</span><span>▭ 22 Comments</span><span>◈ Public_News</span><span>◉ 124 Views</span><span class="love">♥ 12</span></div>
  </article>
</section>

<section class="abs featblog">
  <div class="head blue">Featured Blog News</div>
  <article class="fb-item">
    <div class="img ph-green" role="img" aria-label="Photo of an older couple reading a newspaper in a garden"></div>
    <h3 class="title">At vero eos et accusamus et iusto odio dignissimos ducimus quin the other hand we loreim ipdeno</h3>
    <div class="meta">Posted by jon<b>|</b>2 Comments<b>|</b>4 hours ago</div>
    <p class="excerpt">At vero eos et accusamus et iusto odio dignissimos ducimus qui blanditiis praesentium voluptatum deleniti atque corrupti quos dolores et quas molestias excepturi sint occaecati cupiditate non provident, similique sunt in culpa qui officia deserunt mollitia animi, id est laborum.</p>
    <a class="btn dark">READ MORE</a>
    <div class="metabar"><span>▦ June 11, 2015</span><span>▭ 22 Comments</span><span>◈ Public_News</span><span>◉ 124 Views</span><span class="love">♥ 12</span></div>
  </article>
  <article class="fb-item">
    <div class="img ph-grey" role="img" aria-label="Photo of a person holding an open newspaper"></div>
    <h3 class="title">At vero eos et accusamus et iusto odio dignissimos ducimus quin the other hand we loreim ipdeno</h3>
    <div class="meta">Posted by jon<b>|</b>2 Comments<b>|</b>4 hours ago</div>
    <p class="excerpt">At vero eos et accusamus et iusto odio dignissimos ducimus qui blanditiis praesentium voluptatum deleniti atque corrupti quos dolores et quas molestias excepturi sint occaecati cupiditate non provident, similique sunt in culpa qui officia deserunt mollitia animi, id est laborum.</p>
    <a class="btn dark">READ MORE</a>
    <div class="metabar"><span>▦ June 11, 2015</span><span>▭ 22 Comments</span><span>◈ Public_News</span><span>◉ 124 Views</span><span class="love">♥ 12</span></div>
  </article>
</section>

<div class="abs pager"><span>PAGE 1 OF 2</span><span class="n on">1</span><span class="n">2</span><span class="n">›</span></div>

<!-- sidebar -->
<aside class="abs side" style="top:745px">
  <div class="head blue">Recent Post</div>
  <div class="rp-list">
    <div class="item"><h4>At vero eos et accusamus et iusto odio dimus atiusto odio difei vero eos et accusamus et iusto</h4><div class="meta">3 minute ago<b>|</b>0 comments</div></div>
    <div class="item"><h4>At vero eos et accusamus et iusto odio dimus atiusto odio difei vero eos et accusamus et iusto</h4><div class="meta">3 minute ago<b>|</b>0 comments</div></div>
    <div class="item" style="border:none"><h4>At vero eos et accusamus et iusto odio dimus atiusto odio difei vero eos et accusamus et iusto</h4><div class="meta">3 minute ago<b>|</b>0 comments</div></div>
  </div>
</aside>
<div class="abs side ad" style="top:1114px;height:231px" role="img" aria-label="Sidebar advertisement supporting a sport bid, with a call to action button"></div>
<aside class="abs side" style="top:1391px">
  <div class="head" style="background:#333">Category</div>
  <ul class="cats">
    <li><i></i>Sed ut perspiciatis unde</li>
    <li class="on"><i></i>Iste natus error sit</li>
    <li class="sub"><i></i>Asinanque laudantium</li>
    <li class="sub"><i></i>Lorem ip totaquam dolor utem</li>
    <li><i></i>Auptatem accusantium</li>
    <li><i></i>Wosenque laudantium.</li>
    <li><i></i>Aem speriam, eaque ipsa</li>
    <li><i></i>Wb illo inventore veritatis et</li>
  </ul>
</aside>
<aside class="abs side" style="top:1728px">
  <div class="head blue">Most popular Post<div class="ctl"><span class="on"></span><span></span><span></span></div></div>
  <div class="pop">
    <div class="mini"><div class="img ph-dark" role="img" aria-label="Thumbnail of a man on the phone"></div><div><h4>At vero eos et accusamus et iusto odio dignissimo...</h4><div class="meta">3 minute ago<b>|</b>0 comments</div></div></div>
    <div class="mini"><div class="img ph-blue" role="img" aria-label="Thumbnail of a skyline"></div><div><h4>At vero eos et accusamus et iusto odio dignissimo...</h4><div class="meta">3 minute ago<b>|</b>0 comments</div></div></div>
    <div class="mini"><div class="img ph-blue" role="img" aria-label="Thumbnail of a blue abstract light"></div><div><h4>At vero eos et accusamus et iusto odio dignissimo...</h4><div class="meta">3 minute ago<b>|</b>0 comments</div></div></div>
    <div class="mini"><div class="img ph-grey" role="img" aria-label="Thumbnail of a building facade"></div><div><h4>At vero eos et accusamus et iusto odio dignissimo...</h4><div class="meta">3 minute ago<b>|</b>0 comments</div></div></div>
  </div>
</aside>
<div class="abs side" style="top:2242px;height:214px;background:linear-gradient(180deg,#e3342b,#b51d1a)" role="img" aria-label="Sidebar advertisement for a consumer convention with dates and ticket offer"></div>
<div class="abs side" style="top:2489px;height:231px;background:linear-gradient(180deg,#6fc1ea,#f2f5f7)" role="img" aria-label="Sidebar advertisement for a children's safety day"></div>

<!-- footer -->
<footer class="abs footer">
  <div class="fcol" style="left:132px">
    <h5>About us</h5>
    <div class="name">KITE MAGAZINE</div>
    <div class="tag">Premium News / Magazine</div>
    <p>At vero eos et accusamus et iusto odio dignissimos ducimus qui blanditiis praesentium voluptatum deleniti atque corrupti quos dolores et quas molestias excepturi sint occaecati cupiditate non provident similique.</p>
  </div>
  <div class="fcol" style="left:478px">
    <h5>Recent post</h5>
    <div class="fpost"><div class="img ph-grey" role="img" aria-label="Thumbnail of a city street"></div><div><h6>A New Yorker doesn't necessarily come from...</h6><small>15 hours ago</small></div></div>
    <div class="fpost"><div class="img ph-warm" role="img" aria-label="Thumbnail of a film still"></div><div><h6>Can you guess the most loveyed actor?</h6><small>15 hours ago</small></div></div>
    <div class="fpost"><div class="img ph-green" role="img" aria-label="Thumbnail of a cartoon scene"></div><div><h6>A New Yorker doesn't necessarily come from...</h6><small>15 hours ago</small></div></div>
  </div>
  <div class="fcol news" style="left:824px">
    <h5>Newsletter</h5>
    <p style="width:240px">To receive the latest updates and Latest Posts enter your email</p>
    <div style="margin-top:14px"><input type="text" placeholder="type your email"><span class="go"></span></div>
    <h5 style="margin-top:26px">Connect with Us</h5>
    <div class="fsocial"><span></span><span></span><span></span><span></span><span></span><span></span></div>
  </div>
</footer>
<div class="abs bottombar">
  <div class="l">Disclaimer | Privacy Policy | © 2015 Kite Magazine . all copyrights are reserved</div>
  <div class="r"><span>HOME</span>|<span>ABOUT US</span>|<span>DISCLAIMER</span>|<span>CONTACT US</span></div>
</div>

</body>
</html>
```